Lead Sales Portal Needs to Generate B2B Signup's

We are looking for banner ad designs to drive new business (B2B) traffic to our insurance and mortgage industry self serve lead sites. The sites are HomeLoanProspectHub.com and PolicyBuyerHub.com, and we service over 45,000 insurance agents and mortgage lenders in a self serve lead portal model. We want our banners to generate more of these clients.

Our clients come to our sites, browse our database and then pick out and purchase the consumer leads that they need to generate new business.

We advertise extensively on Zyntrix and on other PPC platforms, and our existing banners are looking really tired.

Some of the ad copy that works well for us is:

Cherry Pick Your Life Leads - Why Pay More Than $3.50 For Life Insurance Leads?
Sign up today and we'll match up to $250

Agents - Here's $250 For New Clients. Cherry Pick Your Life Insurance Leads & Save! Sign up today and we'll match up to $250

One of our Landing Pages that performs well is here:
http://www.policybuyerhub.com/lp/008/

One of our competitors ad's are here:

http://www.brellow.com/search/results?q=QuoteMarten&ad=427360

We're looking for a design that is eye catching, uses our "Deeply Discounted Leads" and our "$250 match bonus"

This is the second contest that we have for the same sites. The previous designs were great and really performed well, so we are looking for new designs now that 6 months have passed. I have uploaded some winning banners from the last group for your information.

Reason: I've been asked by some of the designers to delay a day to get their designs in. I'm happy to do it!

Target Market(s)

These are insurance agents and mortgage lenders. All of our clients are business' or individuals within the business. This is a B2B campaign, so we need something that is professional and upscale. These are NOT consumer facing ad's!

Industry/Entity Type

Insurance

Font styles to use
Sans Serif

Requirements
Must have
• We must have the logos for the sites in the banners. Also, we must have a call to action arrow and "Go" button. Some animation is necessary, (especially around the arrow and the GO button).

One or two designs.

File type

.JPEG
.JPG
.PNG
.GIF

File size

150 KB or smaller

Image sizes

Vertical rectangle: 240 x 400
Mobile leaderboard: 320 x 50
Banner: 468 x 60
Leaderboard: 728 x 90
Square: 250 x 250
Small square: 200 x 200
Large rectangle: 336 x 280
Inline rectangle: 300 x 250
Skyscraper: 120 x 600
Wide skyscraper: 160 x 600
Half-page: 300 x 600
Large leaderboard: 970 x 90

```html
<!DOCTYPE html>
<html lang="en">
<head>
<meta charset="utf-8">
<title>Agents $250 Banner Set</title>
<link rel="stylesheet" href="https://fonts.googleapis.com/css2?family=Bebas+Neue&family=Ubuntu:wght@400&family=Open+Sans:wght@400;700;800&display=swap">
<style>
  :root {
    --stage: #2e1b12;
    --paper: #ffffff;
    --frame: #c9c9c9;
    --green: #8cbf1f;
    --green-band: #8ab71c;
    --ink-head: #4a4a56;
    --ink-body: #55555c;
    --photo-light: #f1efee;
    --photo-mid: #c9b3a6;
    --photo-dark: #2c2a2e;
    --footer: #1f1f21;
    --footer-text: #e6e6e6;
    --go-top: #f2231c;
    --go-bottom: #c40806;
  }
  * { margin: 0; padding: 0; box-sizing: border-box; }
  html, body { width: 1193px; height: 1200px; overflow: hidden; }
  body { background: var(--stage); position: relative; font-family: "Open Sans", sans-serif; }

  .banner {
    position: absolute;
    background: var(--paper);
    border: 2px solid var(--frame);
    overflow: hidden;
  }
  .banner--skyscraper { left: 163px; top: 49px; width: 289px; height: 1084px; }
  .banner--rectangle { left: 486px; top: 49px; width: 542px; height: 452px; }

  .headline {
    font-family: "Bebas Neue", sans-serif;
    color: var(--green);
    line-height: 1;
    position: absolute;
  }
  .subhead {
    font-family: "Bebas Neue", sans-serif;
    color: var(--ink-head);
    line-height: 1;
    position: absolute;
  }
  .pitch {
    font-family: "Ubuntu", sans-serif;
    color: var(--ink-body);
    line-height: 1.03;
    position: absolute;
  }
  .photo { position: absolute; }
  .offer-band {
    position: absolute;
    left: 0; right: 0;
    background: var(--green-band);
    color: #fff;
    font-weight: 700;
    text-align: center;
    text-transform: uppercase;
    display: flex; align-items: center; justify-content: center;
    line-height: 1.2;
  }
  .footer {
    position: absolute;
    left: 0; right: 0; bottom: 0;
    background: var(--footer);
  }
  .brand {
    position: absolute;
    display: flex; align-items: center;
    color: var(--footer-text);
    font-family: "Open Sans", sans-serif;
    font-weight: 400;
    white-space: nowrap;
  }
  .brand-dot {
    border-radius: 50%;
    background: #bdbdbd;
    margin-right: 8px;
    flex: none;
  }
  .cta-arrow { position: absolute; }
  .go-button {
    position: absolute;
    background: linear-gradient(var(--go-top), var(--go-bottom));
    border-radius: 4px;
    display: flex; align-items: center; justify-content: center; gap: 10px;
    color: #fff;
    font-weight: 800;
    font-size: 29px;
    letter-spacing: 1px;
  }
  .go-icon { width: 22px; height: 22px; }

  /* skyscraper */
  .banner--skyscraper .headline { left: 17px; top: 41px; font-size: 76px; }
  .banner--skyscraper .subhead { left: 19px; top: 114px; font-size: 42px; }
  .banner--skyscraper .pitch { left: 21px; top: 213px; font-size: 27px; }
  .banner--skyscraper .photo {
    left: 0; top: 330px; width: 100%; height: 514px;
    background: radial-gradient(ellipse at 50% 40%, var(--photo-mid) 0%, #a9928a 35%, var(--photo-light) 65%), linear-gradient(transparent 70%, var(--photo-dark));
    background-blend-mode: multiply;
  }
  .banner--skyscraper .offer-band { top: 844px; height: 65px; font-size: 21px; }
  .banner--skyscraper .footer { top: 909px; }
  .banner--skyscraper .brand { left: 14px; right: 10px; top: 34px; font-size: 18px; letter-spacing: -0.2px; }
  .banner--skyscraper .brand-dot { width: 24px; height: 24px; margin-right: 7px; }
  .banner--skyscraper .cta-arrow { left: 22px; top: 106px; width: 48px; height: 24px; }
  .banner--skyscraper .go-button { left: 89px; top: 109px; width: 128px; height: 40px; }

  /* rectangle */
  .banner--rectangle .headline { left: 23px; top: 33px; font-size: 74px; }
  .banner--rectangle .subhead { left: 23px; top: 107px; font-size: 42px; }
  .banner--rectangle .pitch { left: 21px; top: 207px; font-size: 27px; }
  .banner--rectangle .photo {
    left: 300px; top: 0; width: 240px; height: 349px;
    background: radial-gradient(ellipse at 55% 35%, var(--photo-mid) 0%, #a9928a 35%, var(--photo-light) 68%), linear-gradient(transparent 60%, var(--photo-dark));
    background-blend-mode: multiply;
  }
  .banner--rectangle .offer-band { top: 349px; height: 31px; font-size: 20px; }
  .banner--rectangle .footer { top: 380px; }
  .banner--rectangle .brand { left: 16px; top: 21px; font-size: 21px; }
  .banner--rectangle .brand-dot { width: 28px; height: 28px; }
  .banner--rectangle .cta-arrow { left: 312px; top: 22px; width: 48px; height: 24px; }
  .banner--rectangle .go-button { left: 381px; top: 16px; width: 128px; height: 40px; }
</style>
</head>
<body>

<section class="banner banner--skyscraper" aria-label="Skyscraper banner 160 by 600">
  <h1 class="headline">AGENTS!</h1>
  <h2 class="subhead">HERE'S $250<br>FOR NEW CLIENTS</h2>
  <p class="pitch">Cherry Pick Your<br>Life Insurance<br>Leads &amp; Save!</p>
  <div class="photo" role="img" aria-label="Portrait of a smiling businesswoman in a dark blazer"></div>
  <p class="offer-band">Sign up today and<br>we'll match up to $250</p>
  <div class="footer">
    <div class="brand"><span class="brand-dot"></span>HomeLoan Prospect Hub</div>
    <svg class="cta-arrow" viewBox="0 0 48 24" aria-hidden="true">
      <path d="M3 10 Q22 8 42 13" fill="none" stroke="#fff" stroke-width="2" stroke-linecap="round"/>
      <path d="M35 7 L43 13 L35 18" fill="none" stroke="#fff" stroke-width="2" stroke-linecap="round" stroke-linejoin="round"/>
    </svg>
    <a class="go-button">GO
      <svg class="go-icon" viewBox="0 0 22 22" aria-hidden="true">
        <circle cx="11" cy="11" r="10" fill="#fff"/>
        <path d="M9 6 L14 11 L9 16" fill="none" stroke="#c40806" stroke-width="3" stroke-linecap="round" stroke-linejoin="round"/>
      </svg>
    </a>
  </div>
</section>

<section class="banner banner--rectangle" aria-label="Inline rectangle banner 300 by 250">
  <h1 class="headline">AGENTS!</h1>
  <h2 class="subhead">HERE'S $250 FOR<br>NEW CLIENTS</h2>
  <p class="pitch">Cherry Pick Your<br>Life Insurance<br>Leads &amp; Save!</p>
  <div class="photo" role="img" aria-label="Portrait of a smiling businesswoman in a dark blazer"></div>
  <p class="offer-band">Sign up today and we'll match up to $250</p>
  <div class="footer">
    <div class="brand"><span class="brand-dot"></span>HomeLoan Prospect Hub</div>
    <svg class="cta-arrow" viewBox="0 0 48 24" aria-hidden="true">
      <path d="M3 10 Q22 8 42 13" fill="none" stroke="#fff" stroke-width="2" stroke-linecap="round"/>
      <path d="M35 7 L43 13 L35 18" fill="none" stroke="#fff" stroke-width="2" stroke-linecap="round" stroke-linejoin="round"/>
    </svg>
    <a class="go-button">GO
      <svg class="go-icon" viewBox="0 0 22 22" aria-hidden="true">
        <circle cx="11" cy="11" r="10" fill="#fff"/>
        <path d="M9 6 L14 11 L9 16" fill="none" stroke="#c40806" stroke-width="3" stroke-linecap="round" stroke-linejoin="round"/>
      </svg>
    </a>
  </div>
</section>

</body>
</html>
```